Business Card Design Project

We are rebranding an existing automotive collision repair business. The business is called dentworks garage. I have attached logo but I'm not tied to that. I want to leave this wide open.

I want this card to say we are professional, competent, cutting edge. We are focused on customers and use a lot of the latest technology to make the customer experience different. We sign customers in on iPads. Paperwork I signed electronically and updates are sent via text, email, logging on a website or as they wish. I want this innovation and image to come through in our cards

Target Market(s)

60%. Women 40% men. Age 35-60

Industry/Entity Type

Automotive

Requirements
Must have
• The card must have name, title, phone,email, cell, web page

```html
<!DOCTYPE html>
<html lang="en">
<head>
<meta charset="utf-8">
<title>Dentworks Garage – Business Card</title>
<link href="https://fonts.googleapis.com/css2?family=Source+Sans+3:wght@300;400;600;700&display=swap" rel="stylesheet">
<style>
  :root {
    --backdrop: #1f1f1f;
    --green-deep: #24802a;
    --green-mid: #4f9d27;
    --green-bright: #80bc24;
    --green-sliver: #8fc43a;
    --ink: #5a5a5a;
    --black: #111111;
    --white: #ffffff;
  }
  * { margin: 0; padding: 0; box-sizing: border-box; }
  html, body {
    width: 1200px; height: 900px; overflow: hidden;
    background: var(--backdrop);
    font-family: "Source Sans 3", sans-serif;
  }
  .canvas { position: relative; width: 1200px; height: 900px; }

  .card {
    position: absolute;
    width: 575px; height: 329px;
    border-radius: 23px;
    overflow: hidden;
  }

  /* Front */
  .card-front {
    left: 294px; top: 107px;
    background: radial-gradient(ellipse 120% 130% at 0% 20%, var(--green-deep) 0%, var(--green-mid) 45%, var(--green-bright) 80%);
    display: flex; align-items: center; justify-content: center;
  }
  .front-name {
    color: var(--white);
    font-weight: 700;
    font-size: 44px;
    letter-spacing: -0.5px;
  }

  /* Back */
  .card-back { left: 292px; top: 463px; background: var(--white); }
  .back-shapes { position: absolute; inset: 0; }
  .back-name {
    position: absolute; left: 30px; top: 60px; width: 230px;
    text-align: center;
    color: var(--green-bright);
    font-weight: 700; font-size: 27px; letter-spacing: -0.3px;
  }
  .address {
    position: absolute; left: 33px; top: 164px;
    color: var(--ink); font-weight: 300; font-size: 15px; line-height: 20px;
  }
  .contacts {
    position: absolute; left: 33px; top: 229px;
    list-style: none;
    color: var(--ink); font-weight: 300; font-size: 15px;
  }
  .contacts li { display: flex; align-items: center; height: 20.5px; }
  .contacts svg { width: 12px; height: 12px; margin-right: 8px; flex: none; }
  .person {
    position: absolute; right: 39px; top: 200px; text-align: right;
    color: var(--white);
  }
  .person-name { font-weight: 600; font-size: 22px; line-height: 26px; }
  .person-title { font-weight: 300; font-size: 15px; line-height: 20px; }
</style>
</head>
<body>
<div class="canvas">

  <section class="card card-front">
    <span class="front-name">Dentworks Garage</span>
  </section>

  <section class="card card-back">
    <svg class="back-shapes" viewBox="0 0 575 329" aria-hidden="true">
      <path d="M307 0 C340 90 345 200 318 295 C330 200 330 90 310 0 Z" fill="var(--green-sliver)"/>
      <path d="M330 0 C362 110 360 240 329 329 L338 329 C364 240 368 110 336 0 Z" fill="var(--black)"/>
      <path d="M336 0 C368 110 364 240 338 329 L575 329 L575 0 Z" fill="var(--green-bright)"/>
    </svg>

    <div class="back-name">Dentworks Garage</div>

    <p class="address">4870 W. Ridgeline Avenue. STE 212<br>Unit 14 Tempe, AZ 85284</p>

    <ul class="contacts">
      <li>
        <svg viewBox="0 0 12 12"><path d="M1 5 Q6 1 11 5 L10 6.5 L8 6 L8 5 Q6 4 4 5 L4 6 L2 6.5 Z" fill="var(--green-bright)"/><rect x="3" y="7" width="6" height="3.5" rx="0.8" fill="var(--green-bright)"/></svg>
        800-555-0192
      </li>
      <li>
        <svg viewBox="0 0 12 12"><rect x="1" y="8" width="2" height="3" fill="var(--green-bright)"/><rect x="4" y="6" width="2" height="5" fill="var(--green-bright)"/><rect x="7" y="4" width="2" height="7" fill="var(--green-bright)"/><rect x="10" y="2" width="1.6" height="9" fill="var(--green-bright)"/></svg>
        800-555-0192
      </li>
      <li>
        <svg viewBox="0 0 12 12"><rect x="1" y="2.5" width="10" height="7" fill="none" stroke="var(--green-bright)" stroke-width="1"/><path d="M1 2.5 L6 6.5 L11 2.5" fill="none" stroke="var(--green-bright)" stroke-width="1"/></svg>
        info@dentworksgarage.com
      </li>
      <li>
        <svg viewBox="0 0 12 12"><circle cx="6" cy="6" r="5" fill="var(--green-bright)"/><path d="M1 6 H11 M6 1 Q3 6 6 11 M6 1 Q9 6 6 11" fill="none" stroke="var(--white)" stroke-width="0.7"/></svg>
        www.dentworksgarage.com
      </li>
    </ul>

    <div class="person">
      <div class="person-name">Marcus Hale</div>
      <div class="person-title">Vice President</div>
    </div>
  </section>

</div>
</body>
</html>
```